Systems and Technology Consultants - Website

Design & Build a website for a new company which operates in the Systems and Technology space for Transportation, Government and Commercial sectors.

Overall design should be minimalist in nature.
Should also have a feed that provides news and event updates on the main page.
Logo has already been awarded and should be incorporated into the site.

We like the overall layout, functionality and simplicity of the below sites. Submitted designs could be similar to or a combination of the aspects on these sites, or perhaps a whole different concept - we are open to new ideas.
Vortrane.com
Merp.it

Update 1 Dated 27 May 2014

All I am moving away from the Merp.it website and would like it to be more aligned with Vortrane.com not only in layout but in functionality. I will be extending the deadline of this design brief for two weeks to incorporate additional requirements and will add addtional funding to the project.

Apologies for not having more information available to provide but with so many submissions its getting confusing.

Thanks Dermot
Updates

Please note that the brief has been updated and the deadline has been extended.

Important: We will need two language versions of the website, English and Arabic; the website is hosted on HostPeak

Hello All, Thank you for your submissions. We have narrowed it down to the final 6 designers and I just wanted to take a moment and provide a bit of feedback regarding the concepts that we like and the modifications we are looking for. First, let me mention some of the design functions we like. - At the top of the homepage we really like the "region" or "language" tab so that the website can be viewed in both English and Arabic. - We like the homepage to have clear color variation so that the different sections of the homepage are distinct. Additionally, we like the bottom portion of the homepage to be in red. We feel that draws attention to our contact information. Again, we would like the colors to integrate black, gray-scale, red, etc. - Having a search tab at the top of the home page, or integrated into the main image, so that the site is easy to navigate. - We especially like the main image to have the scrolling tabs at the bottom so it is easy to browse the services offered (Consultancy, Solutions Architecture, Masters Systems Integration, Independent Design Review). - In regards to the services offered tab we really like the idea that a few people presented that have the outside of our logo with an icon in the middle of consultancy, solutions, etc., etc. Secondly, as mentioned in our brief we really enjoy the design of vortrane site. Specially, we enjoy the strong iconic images they use, the way the tabs at the top scroll easily, and contact us page that generates an email. Lastly, I've included some photos of the concept we have been working on. What we are trying to demonstrate is how our company offers a range of services that are essentially linked together. We provide individual services that when combined present the full service package. We would like this concept to be integrated into the over concept of our website. Please feel free to ask for clarification of any of the above points or contact us if you have any additional questions. We appreciate all of your hard work and are very excited to see the updated designs. Best, Miriam Dowbrook Plenvaro Senior Program Manager miriam.dowbrook@plenvaro-mail.com

Industry/Entity Type

Government

Font styles to use
Serif
Sans Serif

Requirements
Must have
• Must work on/adapt to various/mobile devices (responsive)
Must be simple and straightforward
Colors should be in line/matching with logo
2 language versions: English and Arabic (no Thai)
Services should be the first group/row of items after/below the main image
Note: the website will be hosted by hostpeak
Nice to have
• Submit feedback form
What's New section
The banner at the bottom of the site should not be too large; we would like a narrow one more
It would be nice if the header/top banner (with Home, About, etc. tabs) could stay in place as you scroll down (like Vortrane and Chatterly)
We will likely only use one image with a Company slogan on the Home page rather than a carousel of images to rotate through
Should not have
• This is the existing website: http://www.plenvaro-example.org
We do not like the animation, the way the banner icons/titles bounce
Not simple enough, we don't like the functionality or how pages load so slowly
We do not like the logo centered - it should be at the left
The banner and its tabs should not be towards the right, we would like them to be centered, to go all the way across and to be below the logo

```html
<!DOCTYPE html>
<html lang="en">
<head>
<meta charset="utf-8">
<title>Plenvaro Technik — Systems Knowledge Delivered</title>
<link href="https://fonts.googleapis.com/css2?family=Open+Sans:wght@400;600;700&family=Roboto:wght@700;900&display=swap" rel="stylesheet">
<style>
:root{
  --red:#c8161d;
  --dark:#1f1f1f;
  --darker:#161616;
  --ink:#222;
  --muted:#6f6f6f;
  --light:#f1f1f1;
  --line:#d9d9d9;
  --white:#fff;
}
*{margin:0;padding:0;box-sizing:border-box}
html,body{width:1200px;height:2672px;overflow:hidden}
body{font-family:"Open Sans",Arial,sans-serif;color:var(--ink);background:var(--white);position:relative}
.abs{position:absolute}

/* header */
.site-header{position:absolute;left:0;top:0;width:1200px;height:220px;background:linear-gradient(#262626,#1a1a1a)}
.topbar-search{position:absolute;left:860px;top:8px;width:190px;height:22px;background:var(--white);border-radius:3px}
.topbar-search span{position:absolute;right:0;top:0;width:26px;height:22px;background:var(--red);border-radius:0 3px 3px 0}
.social{position:absolute;top:8px;width:22px;height:22px;border-radius:50%;background:var(--white)}
.brand{position:absolute;left:112px;top:60px;display:flex;align-items:center;gap:16px}
.brand-mark{width:52px;height:52px;background:var(--red)}
.brand-name{font-family:"Roboto",Arial,sans-serif;font-weight:900;font-size:40px;color:var(--white);letter-spacing:2px}
.main-nav{position:absolute;top:112px;left:312px;right:0;display:flex;align-items:center}
.main-nav a{font-family:"Open Sans",Arial,sans-serif;font-weight:600;font-size:17px;color:var(--white);text-decoration:none;margin-right:60px;padding:6px 0}
.main-nav a.active{background:var(--red);border-radius:14px;padding:6px 24px;margin-right:36px}

/* hero */
.hero{position:absolute;left:0;top:220px;width:1200px;height:548px;background:linear-gradient(90deg,#e9e9e9,#f6f6f6 60%,#e4e4e4)}
.hero-photo{position:absolute;left:80px;top:40px;width:320px;height:508px;background:linear-gradient(#dfe3e8,#aab4c2)}
.hero-title{position:absolute;left:592px;top:98px;font-family:"Roboto",Arial,sans-serif;font-weight:900;font-size:66px;line-height:70px;color:#1b1b1b;letter-spacing:2px}
.hero-title .accent{color:var(--red)}
.hero-copy{position:absolute;left:592px;top:312px;width:420px;font-size:16px;line-height:24px;color:#555}

/* welcome */
.welcome{position:absolute;left:0;top:768px;width:1200px;height:420px}
.section-title{font-size:24px;text-align:center;color:#444}
.section-title b{color:var(--red);font-weight:700}
.welcome .section-title{position:absolute;top:60px;width:100%}
.welcome-mark{position:absolute;left:588px;top:104px;width:24px;height:24px;background:var(--red)}
.welcome-copy{position:absolute;left:140px;width:920px;text-align:center;font-size:15px;line-height:26px;color:#666}

/* services */
.services{position:absolute;left:0;top:1196px;width:1200px;height:520px;background:var(--light);border-top:1px solid var(--line)}
.services .section-title{position:absolute;top:40px;width:100%}
.carousel-arrows{position:absolute;right:40px;top:40px;display:flex;gap:8px;font-size:20px;color:#333}
.service{position:absolute;top:124px;width:280px;text-align:center}
.service-icon{width:140px;height:140px;margin:0 auto;background:linear-gradient(#fff,#e6e6e6);border-radius:16px;box-shadow:0 4px 10px rgba(0,0,0,.15);display:flex;align-items:center;justify-content:center}
.service h3{margin-top:30px;font-size:18px;font-weight:700;color:var(--red)}
.service p{margin-top:16px;font-size:15px;line-height:22px;color:#666}
.btn{display:inline-block;margin-top:20px;background:#a1161a;color:var(--white);font-size:14px;padding:6px 26px;border-radius:14px;text-decoration:none}

/* news */
.whats-new{position:absolute;left:0;top:1716px;width:1200px;height:516px}
.whats-new h2{position:absolute;left:80px;top:64px;font-size:26px;font-weight:400;color:#333}
.whats-new h2 b{color:var(--red)}
.news-rule{position:absolute;left:80px;top:118px;width:1040px;height:1px;background:var(--line)}
.article{position:absolute;left:96px;width:560px}
.article-thumb{position:absolute;left:0;top:0;width:144px;height:112px;background:linear-gradient(#a9c7e4,#8aa65a)}
.article h4{position:absolute;left:176px;top:0;font-size:15px;font-weight:700;color:var(--red)}
.article p{position:absolute;left:176px;top:26px;width:300px;font-size:15px;line-height:22px;color:#555}
.monitor{position:absolute;left:720px;top:156px;width:408px;height:288px;background:linear-gradient(#e8e8e8,#c9c9c9);border-radius:6px}

/* footer */
.site-footer{position:absolute;left:0;top:2232px;width:1200px;height:392px;background:var(--dark)}
.foot-col{position:absolute;top:92px}
.foot-col h5{font-size:17px;font-weight:600;color:var(--white);margin-bottom:22px}
.foot-col li{list-style:none;font-size:15px;color:#ddd;padding:8px 0;border-bottom:1px solid #333;width:190px}
.foot-col li::before{content:"› ";color:#aaa}
.contact-line{display:flex;align-items:center;gap:10px;font-size:14px;color:#ddd;margin-bottom:12px}
.foot-social{display:flex;gap:10px;margin-top:8px}
.foot-social span{width:24px;height:24px;border-radius:50%;background:var(--white)}
.newsletter p{font-size:14px;color:#ccc;margin-bottom:10px}
.newsletter .field{width:200px;height:28px;background:var(--white);font-size:13px;color:#999;padding:5px 8px}
.newsletter .submit{display:inline-block;margin-top:14px;background:var(--red);color:var(--white);font-size:13px;padding:4px 26px}
.bottom-bar{position:absolute;left:0;top:2624px;width:1200px;height:48px;background:var(--darker);display:flex;justify-content:space-between;align-items:center;padding:0 80px;font-size:13px;color:var(--red)}
.bottom-bar .links{color:#ccc}
</style>
</head>
<body>

<header class="site-header">
  <div class="topbar-search"><span></span></div>
  <div class="social" style="left:1066px"></div>
  <div class="social" style="left:1094px"></div>
  <div class="social" style="left:1122px"></div>
  <div class="brand"><div class="brand-mark"></div><div class="brand-name">PLENVARO</div></div>
  <nav class="main-nav">
    <a class="active" href="#">HOME</a>
    <a href="#">BUSINESS UNIT</a>
    <a href="#">SERVICES</a>
    <a href="#">ABOUT US</a>
    <a href="#">LOCATIONS</a>
    <a href="#">CONTACT US</a>
  </nav>
</header>

<section class="hero">
  <div class="hero-photo" role="img" aria-label="Engineer in white hard hat and tie, arms crossed"></div>
  <h1 class="hero-title">SYSTEMS<br><span class="accent">KNOWLEDGE</span><br>DELIVERED</h1>
  <p class="hero-copy">Lorem ipsum dolor sit amet, consectetur adipi scing elit. Phasellus tincidunt tellus leo. Cum sociis natoque penatibus et magnis dis parturient montes, nascetur ridiculus mus. Sed sagittis laoreet dolor non tempus.</p>
</section>

<section class="welcome">
  <h2 class="section-title">Welcome to <b>Plenvaro Technik</b></h2>
  <div class="welcome-mark"></div>
  <p class="welcome-copy" style="top:156px">Lorem ipsum dolor sit amet, consectetur adipiscing elit. Phasellus tincid unt tellus leo, sodales vestibulum urna hendrerit vel. Maecenas ut pre tium tortor. sodales vestibulum urna hendrerit vel. Mae cenas ut pretium tortor.hendrerit vel. Maece nas ut pretium tortor. Sodales vestibulum urna hendrerit vel. Maecenas.</p>
  <p class="welcome-copy" style="top:284px">Maecenas ut pretium tortor.sodales vestibulum urna hendrerit vel. Maecenas ut pretium tortor.hendrerit vel. Maecenas ut pretium tortor.sodales vestibulum urna hendrerit vel. Maecenas ut pretium tortor. Vestibulum urna hendrerit vel. Maec cenas ut pretium tortor.hendrerit vel.</p>
</section>

<section class="services">
  <h2 class="section-title">Featured <b>Services</b></h2>
  <div class="carousel-arrows"><span>‹</span><span>›</span></div>

  <div class="service" style="left:152px">
    <div class="service-icon">
      <svg width="70" height="70" viewBox="0 0 70 70"><g stroke="#b0151b" stroke-width="9" stroke-linecap="round"><line x1="14" y1="14" x2="56" y2="56"/><line x1="56" y1="14" x2="14" y2="56"/></g></svg>
    </div>
    <h3>CONSTRUCTION</h3>
    <p>Lorem ipsum dolor sit amet, consect etur adipiscing elit. Ut felis ligula dil agnis sed amet interdum non, labore.</p>
    <a class="btn" href="#">Read more</a>
  </div>

  <div class="service" style="left:460px">
    <div class="service-icon">
      <svg width="70" height="70" viewBox="0 0 70 70"><g fill="none" stroke="#222" stroke-width="7"><circle cx="26" cy="30" r="13" stroke-dasharray="6 4"/><circle cx="50" cy="48" r="8" stroke-dasharray="4 3"/></g></svg>
    </div>
    <h3>ENGINEERING</h3>
    <p>Lorem ipsum dolor sit amet, consect etur adipiscing elit. Ut felis ligula dil agnis sed amet interdum non, labore.</p>
    <a class="btn" href="#">Read more</a>
  </div>

  <div class="service" style="left:772px">
    <div class="service-icon">
      <svg width="70" height="70" viewBox="0 0 70 70"><g fill="#b0151b"><circle cx="20" cy="18" r="7"/><circle cx="50" cy="18" r="7"/><circle cx="35" cy="34" r="7"/><rect x="13" y="27" width="14" height="20" rx="3"/><rect x="43" y="27" width="14" height="20" rx="3"/><rect x="28" y="43" width="14" height="20" rx="3"/></g></svg>
    </div>
    <h3>CONSULTING</h3>
    <p>Lorem ipsum dolor sit amet, consect etur adipiscing elit. Ut felis ligula dil agnis sed amet interdum non, labore.</p>
    <a class="btn" href="#">Read more</a>
  </div>
</section>

<section class="whats-new">
  <h2>What's <b>New?</b></h2>
  <div class="news-rule"></div>
  <article class="article" style="top:164px">
    <div class="article-thumb" role="img" aria-label="Engineer on site with blue sky"></div>
    <h4>ARTICLE TITLE GOES HERE</h4>
    <p>Lorem ipsum dolor sit amet, consectetur adipi scing elit. Phasellus tinc. Sed adipiscing mi orci, vel ultrices turpis mattis a lacinia elit dolor.</p>
  </article>
  <article class="article" style="top:324px">
    <div class="article-thumb" role="img" aria-label="Engineer surveying a green field"></div>
    <h4>ARTICLE TITLE GOES HERE</h4>
    <p>Lorem ipsum dolor sit amet, consectetur adipi scing elit. Phasellus tinc. Sed adipiscing mi orci, vel ultrices turpis mattis a lacinia elit dolor.</p>
  </article>
  <div class="monitor" role="img" aria-label="Desktop monitor showing the company name"></div>
</section>

<footer class="site-footer">
  <div class="foot-col" style="left:80px">
    <h5>Who we are</h5>
    <ul><li>Subline here</li><li>Subline here</li><li>Subline here</li><li>Subline here</li></ul>
  </div>
  <div class="foot-col" style="left:336px">
    <h5>What we offer</h5>
    <ul><li>Subline here</li><li>Subline here</li><li>Subline here</li><li>Subline here</li></ul>
  </div>
  <div class="foot-col" style="left:600px">
    <h5>Contact us</h5>
    <div class="contact-line"><svg width="16" height="12" viewBox="0 0 16 12"><rect x="0.5" y="0.5" width="15" height="11" fill="none" stroke="#ddd"/><path d="M1 1l7 6 7-6" fill="none" stroke="#ddd"/></svg>Youroffice@email.com</div>
    <div class="contact-line"><svg width="14" height="14" viewBox="0 0 14 14"><path d="M3 1l3 3-2 2c1 2 2 3 4 4l2-2 3 3-2 2C6 13 1 8 1 3z" fill="#ddd"/></svg>02-1234-456</div>
    <div class="foot-social"><span></span><span></span><span></span></div>
  </div>
  <div class="foot-col newsletter" style="left:904px">
    <h5>Newsletter Signup</h5>
    <p>Subscribe to get updates</p>
    <div class="field">Email address</div>
    <span class="submit">SUBMIT</span>
  </div>
</footer>
<div class="bottom-bar">
  <span>Copyright © 2014 Plenvaro Tech</span>
  <span class="links">FAQ &nbsp;|&nbsp; Sitemap &nbsp;|&nbsp; Privacy Policy</span>
</div>

</body>
</html>
```